HR Technology Company (Corvexa) needs a consistent powerpoint deck for future presentations

We are Corvexa (corvexa-example.com). You can visit our website for colours scheme etc. I am looking for a full PPT pack which can be used for various presentations in the future. Sales Presentation, Company Overview etc. This must include charts, graphs, services (4/6/8 items), people slide, timeline slides etc among all the other common slides.

```html
<!DOCTYPE html>
<html lang="en">
<head>
<meta charset="utf-8">
<title>Corvexa – Presentation Deck</title>
<link href="https://fonts.googleapis.com/css2?family=Montserrat:wght@400;500;600;700;800&display=swap" rel="stylesheet">
<style>
:root{
  --orange:#f58220;
  --dark:#231f20;
  --panel:#e7e7e8;
  --text:#5b5b5b;
  --line:#d9d9d9;
  --stage:#c8c8c9;
  --white:#ffffff;
}
*{box-sizing:border-box;margin:0;padding:0}
html,body{width:1031px;height:1200px;overflow:hidden}
body{font-family:"Montserrat",sans-serif;background:var(--stage)}
.canvas{position:relative;width:1031px;height:1200px;overflow:hidden;background:linear-gradient(160deg,#d2d2d3,#bdbdbe)}
.slide{position:absolute;width:608px;height:342px;background:var(--white);transform:scale(.5);transform-origin:0 0;overflow:hidden;box-shadow:4px 6px 10px rgba(0,0,0,.35)}
.abs{position:absolute}
.brand{position:absolute;top:14px;right:18px;font-size:12px;font-weight:600;color:var(--dark);display:flex;align-items:center;gap:4px}
.sq{display:inline-block;width:8px;height:8px;background:var(--orange)}
.foot{position:absolute;left:0;right:0;bottom:10px;height:1.5px;background:var(--orange)}
.pg{position:absolute;right:14px;bottom:5px;width:22px;height:12px;background:var(--dark);color:#fff;font-size:7px;font-weight:700;text-align:center;line-height:12px}
.h2{position:absolute;font-size:22px;line-height:1.05;font-weight:500;color:var(--dark);text-transform:uppercase}
.h2 b{display:block;color:var(--orange);font-weight:700}
.h2 .o{color:var(--orange);font-weight:700}
.tx{font-size:6.4px;line-height:1.45;color:var(--text);text-align:justify}
.tx+.tx{margin-top:7px}
.it{font-size:10px;font-weight:700;color:var(--orange);margin-bottom:3px}
.it.d{color:var(--dark)}
.photo{position:absolute}
.tri{display:flex;gap:10px;align-items:flex-start}
.tri i{width:0;height:0;border-top:4px solid transparent;border-bottom:4px solid transparent;border-left:7px solid var(--orange);flex:none;margin-top:1px}
.tri i.hollow{border-left-color:transparent;position:relative}
.tri i.hollow::after{content:"";position:absolute;left:-7px;top:-4px;width:0;height:0;border-top:4px solid transparent;border-bottom:4px solid transparent;border-left:7px solid var(--text);opacity:.6}
.center{text-align:center}
svg text{font-family:"Montserrat",sans-serif}
</style>
</head>
<body>
<div class="canvas">

<!-- 01 Cover -->
<section class="slide" style="left:48px;top:53px">
  <div class="abs" style="left:26px;top:40px;font-size:30px;font-weight:600;color:var(--dark);display:flex;align-items:center;gap:8px"><span class="sq" style="width:14px;height:14px"></span>Corvexa</div>
  <p class="abs" style="left:26px;top:150px;font-size:16px;font-weight:500;color:var(--dark)">PRESENTATION</p>
  <p class="abs" style="left:24px;top:168px;font-size:42px;font-weight:800;color:var(--dark)">BUSINESS</p>
  <p class="abs" style="left:24px;top:216px;font-size:42px;font-weight:800;color:var(--orange)">MARKETING</p>
  <div class="abs" style="left:26px;top:284px;width:185px;height:1.5px;background:var(--dark)"></div>
  <p class="abs" style="left:26px;top:296px;font-size:13px;letter-spacing:5px;color:var(--orange)">corvexa-example.com</p>
  <div class="photo" role="img" aria-label="Photo of a smiling woman on the phone at a laptop in a bright office" style="left:316px;top:0;width:292px;height:342px;background:linear-gradient(120deg,#eeeeee,#d9d2cb 55%,#b8aca2)"></div>
</section>

<!-- 02 Contents -->
<section class="slide" style="left:364px;top:53px">
  <div class="brand"><span class="sq"></span>Corvexa</div>
  <div class="photo" role="img" aria-label="Photo of a smiling support agent wearing a headset" style="left:16px;top:23px;width:275px;height:296px;background:linear-gradient(135deg,#e4e4e4,#b9b4ae 60%,#8f8a86)"></div>
  <div class="abs" style="left:192px;top:156px;background:#fff;padding:2px 6px;border-radius:10px;font-size:27px;font-weight:700;color:var(--orange)">Contents</div>
  <svg class="abs" style="left:0;top:0" width="608" height="342">
    <path d="M338 68V262M320 165H338M338 68H346M338 126H346M338 196H346M338 262H346" stroke="#555" stroke-width="1" fill="none"/>
  </svg>
  <div class="abs" style="left:350px;top:60px;width:200px">
    <p class="it">Lorem ipsum</p><p class="tx">We shape hiring plans that grow with your teams and goals.</p>
  </div>
  <div class="abs" style="left:350px;top:118px;width:200px">
    <p class="it">Lorem ipsum</p><p class="tx">Simple onboarding flows that welcome every new starter well.</p>
  </div>
  <div class="abs" style="left:350px;top:188px;width:200px">
    <p class="it">Lorem ipsum</p><p class="tx">Clear reports that show how your people and teams perform.</p>
  </div>
  <div class="abs" style="left:350px;top:254px;width:200px">
    <p class="it">Lorem ipsum</p><p class="tx">Friendly support from a team that knows HR inside and out.</p>
  </div>
  <div class="foot"></div><div class="pg">02</div>
</section>

<!-- 03 Intro -->
<section class="slide" style="left:680px;top:53px">
  <div class="brand"><span class="sq"></span>Corvexa</div>
  <h2 class="h2" style="left:38px;top:48px">Lorem ipsum<b>dolor sit amet</b></h2>
  <div class="abs" style="left:38px;top:104px;width:290px">
    <p class="tx">Corvexa builds people tools for modern companies. We help teams find, hire and keep great talent with less paperwork and more care. Our platform brings hiring, onboarding, reviews and payroll data into one clear space, so managers can act fast and staff feel heard at every stage of their journey.</p>
    <p class="tx">From small startups to large groups, our clients trust us to turn HR from a cost into a real driver of growth and team spirit.</p>
    <p class="tx">We listen first, plan together and deliver tools that fit the way your people already work, with support that stays close long after launch.</p>
  </div>
  <svg class="abs" style="left:0;top:0" width="608" height="342" fill="none" stroke="var(--orange)" stroke-width="1.5">
    <circle cx="406" cy="102" r="20"/><circle cx="523" cy="102" r="20"/><circle cx="406" cy="217" r="20"/><circle cx="523" cy="217" r="20"/>
    <path d="M400 95h12l3 14h-18z M403 95l3-5 3 5"/>
    <rect x="513" y="93" width="20" height="13"/><path d="M517 102l4-4 3 3 5-5"/>
    <rect x="396" y="208" width="20" height="14"/><path d="M400 216h12"/>
    <path d="M515 226v-8M521 226v-12M527 226v-16M531 226v-6"/>
  </svg>
  <div class="abs center" style="left:366px;top:128px;width:80px"><p class="it" style="font-size:8px">LOREM IPSUM</p><p class="tx center" style="font-size:5.5px">Smart tools that save time for busy teams.</p></div>
  <div class="abs center" style="left:483px;top:128px;width:80px"><p class="it" style="font-size:8px">LOREM IPSUM</p><p class="tx center" style="font-size:5.5px">Live dashboards for every people metric.</p></div>
  <div class="abs center" style="left:366px;top:243px;width:80px"><p class="it" style="font-size:8px">LOREM IPSUM</p><p class="tx center" style="font-size:5.5px">Hiring flows that bring the right fit in.</p></div>
  <div class="abs center" style="left:483px;top:243px;width:80px"><p class="it" style="font-size:8px">LOREM IPSUM</p><p class="tx center" style="font-size:5.5px">Growth plans built on clear, fair data.</p></div>
  <div class="foot"></div><div class="pg">03</div>
</section>

<!-- 04 Data -->
<section class="slide" style="left:48px;top:237px">
  <div class="brand"><span class="sq"></span>Corvexa</div>
  <div class="abs" style="left:25px;top:36px;width:287px;height:274px;background:var(--panel)"></div>
  <h2 class="h2" style="left:45px;top:62px">Data our<b>company</b></h2>
  <div class="abs" style="left:45px;top:130px;width:240px">
    <p class="tx">Our data team turns raw HR records into clear insight. We track hiring speed, staff turnover, team growth and training results, then share simple reports that leaders can read in minutes and act on the same day. Every number is checked, secure and easy to trace back to its source.</p>
    <p class="tx">With clean data in one place, you can plan headcount, spot risk early and reward the people who make your company stronger.</p>
  </div>
  <svg class="abs" style="left:0;top:0" width="608" height="342" fill="#fff" stroke="var(--dark)" stroke-width="1.5">
    <circle cx="312" cy="75" r="21"/><circle cx="312" cy="165" r="21"/><circle cx="312" cy="255" r="21"/>
    <g stroke="var(--orange)" fill="none"><rect x="302" y="68" width="16" height="12"/><circle cx="318" cy="82" r="4"/>
    <path d="M302 165a6 6 0 0 1 6-6a7 7 0 0 1 13 2a4 4 0 0 1 0 8h-19a4 4 0 0 1 0-4z"/>
    <path d="M301 262l7-8 6 4 9-10"/></g>
  </svg>
  <div class="abs" style="left:350px;top:64px;width:210px"><p class="it">Lorem ipsum</p><p class="tx">Secure records for every employee, stored safely and kept up to date with each change made.</p></div>
  <div class="abs" style="left:350px;top:154px;width:210px"><p class="it">Lorem ipsum</p><p class="tx">Cloud access from any device, so managers can review and approve on the go at any time.</p></div>
  <div class="abs" style="left:350px;top:244px;width:210px"><p class="it">Lorem ipsum</p><p class="tx">Linked insights that join hiring, pay and reviews to show the full story behind growth.</p></div>
  <div class="foot"></div><div class="pg">04</div>
</section>

<!-- 05 Overview -->
<section class="slide" style="left:364px;top:237px">
  <div class="brand"><span class="sq"></span>Corvexa</div>
  <h2 class="h2" style="left:25px;top:35px">Company<b style="font-size:30px;font-weight:600">overview</b></h2>
  <div class="abs" style="left:25px;top:102px;width:250px">
    <p class="tx">Corvexa was founded to make HR simple for every team. Today we support hundreds of firms with hiring, onboarding, reviews and people data, helping them grow faster with happier staff.</p>
    <p class="tx">Our products are built by HR experts and engineers working side by side.</p>
  </div>
  <svg class="abs" style="left:0;top:0" width="608" height="342" font-size="7" fill="#555">
    <g stroke="#e2e2e2" stroke-width=".8"><path d="M300 62H555M300 81H555M300 100H555M300 119H555M300 138H555M300 157H555M300 175H555"/></g>
    <text x="290" y="64" text-anchor="end">60</text><text x="290" y="83" text-anchor="end">50</text><text x="290" y="102" text-anchor="end">40</text><text x="290" y="121" text-anchor="end">30</text><text x="290" y="140" text-anchor="end">20</text><text x="290" y="159" text-anchor="end">10</text><text x="290" y="177" text-anchor="end">0</text>
    <rect x="336" y="100" width="7" height="75" fill="var(--dark)"/><rect x="346" y="81" width="7" height="94" fill="var(--orange)"/>
    <rect x="390" y="152" width="7" height="23" fill="var(--dark)"/><rect x="400" y="109" width="7" height="66" fill="var(--orange)"/>
    <rect x="445" y="66" width="7" height="109" fill="var(--dark)"/><rect x="455" y="151" width="7" height="24" fill="var(--orange)"/>
    <rect x="503" y="77" width="7" height="98" fill="var(--orange)"/><rect x="513" y="119" width="7" height="56" fill="var(--dark)"/>
    <text x="345" y="190" text-anchor="middle">JAN</text><text x="399" y="190" text-anchor="middle">FEB</text><text x="454" y="190" text-anchor="middle">MAR</text><text x="512" y="190" text-anchor="middle">APR</text>
    <g stroke="#e2e2e2" stroke-width=".8"><path d="M40 205H255M40 221H255M40 237H255M40 252H255M40 268H255M40 284H255M40 300H255"/></g>
    <g font-size="6"><text x="34" y="207" text-anchor="end">60</text><text x="34" y="223" text-anchor="end">50</text><text x="34" y="239" text-anchor="end">40</text><text x="34" y="254" text-anchor="end">30</text><text x="34" y="270" text-anchor="end">20</text><text x="34" y="286" text-anchor="end">10</text><text x="34" y="302" text-anchor="end">0</text></g>
    <polyline points="50,281 75,292 100,262 125,224 150,245 175,268 200,256 225,284 250,252" fill="none" stroke="var(--orange)" stroke-width="1.2"/>
    <polyline points="50,297 75,287 100,260 125,284 150,240 175,260 200,268 225,245 250,237" fill="none" stroke="var(--dark)" stroke-width="1.2"/>
    <g font-size="4.5"><text x="50" y="310" text-anchor="middle">TEXT 01</text><text x="75" y="310" text-anchor="middle">TEXT 02</text><text x="100" y="310" text-anchor="middle">TEXT 03</text><text x="125" y="310" text-anchor="middle">TEXT 04</text><text x="150" y="310" text-anchor="middle">TEXT 05</text><text x="175" y="310" text-anchor="middle">TEXT 06</text><text x="200" y="310" text-anchor="middle">TEXT 07</text><text x="225" y="310" text-anchor="middle">TEXT 08</text><text x="250" y="310" text-anchor="middle">TEXT 09</text></g>
    <circle cx="298" cy="222" r="3.5" fill="var(--dark)"/><circle cx="425" cy="222" r="3.5" fill="var(--orange)"/><circle cx="298" cy="266" r="3.5" fill="var(--orange)"/><circle cx="425" cy="266" r="3.5" fill="var(--dark)"/>
  </svg>
  <div class="abs" style="left:308px;top:216px;width:105px"><p class="it d" style="font-size:8px">Lorem ipsum</p><p class="tx" style="font-size:5px">Hiring rate across the first four months of the year.</p></div>
  <div class="abs" style="left:435px;top:216px;width:105px"><p class="it" style="font-size:8px">Lorem ipsum</p><p class="tx" style="font-size:5px">Onboarding done on time across each new team.</p></div>
  <div class="abs" style="left:308px;top:260px;width:105px"><p class="it" style="font-size:8px">Lorem ipsum</p><p class="tx" style="font-size:5px">Review scores shared by managers this quarter.</p></div>
  <div class="abs" style="left:435px;top:260px;width:105px"><p class="it d" style="font-size:8px">Lorem ipsum</p><p class="tx" style="font-size:5px">Staff who stayed with us through the full year.</p></div>
  <div class="foot"></div><div class="pg">05</div>
</section>

<!-- 06 Intelligence -->
<section class="slide" style="left:680px;top:237px">
  <div class="brand"><span class="sq"></span>Corvexa</div>
  <h2 class="h2" style="left:30px;top:38px">Active<b>intelligence</b></h2>
  <div class="abs" style="left:30px;top:92px;width:245px">
    <p class="tx">Our smart engine reads patterns in your people data and points out what needs care. It flags teams at risk of burnout, highlights rising stars and suggests training before gaps appear, so leaders act early instead of late.</p>
    <p class="tx">Every suggestion is explained in plain words, with the data behind it one click away, so decisions stay fair, open and human at every step.</p>
  </div>
  <div class="abs" style="left:428px;top:60px;width:180px;height:2px;background:var(--dark)"></div>
  <div class="photo" role="img" aria-label="Photo of hands typing on a laptop showing charts and dashboards" style="left:300px;top:70px;width:308px;height:220px;background:linear-gradient(135deg,#e9ecef,#b9c3cc 55%,#7d8790)"></div>
  <div class="abs tri" style="left:30px;top:242px;width:245px"><i></i><p class="tx">Alerts that reach the right manager at the right time every day.</p></div>
  <div class="abs tri" style="left:30px;top:275px;width:245px"><i class="hollow"></i><p class="tx">Forecasts that help you plan staffing for the months ahead.</p></div>
  <div class="foot"></div><div class="pg">06</div>
</section>

<!-- 07 Market -->
<section class="slide" style="left:48px;top:425px">
  <div class="brand"><span class="sq"></span>Corvexa</div>
  <h2 class="h2" style="left:25px;top:30px">Market<b>opportunities</b></h2>
  <div class="abs" style="left:25px;top:98px;width:260px">
    <p class="tx">Demand for simple HR tools keeps rising as firms grow remote teams and compete for talent. We see strong room to expand in mid-size firms that need one clear platform for people work.</p>
    <p class="tx">New regions and sectors are opening up fast.</p>
  </div>
  <p class="abs" style="left:305px;top:32px;font-size:7px;font-weight:600;color:var(--dark)">CONSECTETUER ADIPISCING</p>
  <svg class="abs" style="left:0;top:0" width="608" height="342" font-size="7" fill="#555">
    <g stroke="#e2e2e2" stroke-width=".8"><path d="M318 62H555M318 80H555M318 97H555M318 115H555M318 133H555M318 150H555M318 168H555"/></g>
    <text x="310" y="64" text-anchor="end">60</text><text x="310" y="82" text-anchor="end">50</text><text x="310" y="99" text-anchor="end">40</text><text x="310" y="117" text-anchor="end">30</text><text x="310" y="135" text-anchor="end">20</text><text x="310" y="152" text-anchor="end">10</text><text x="310" y="170" text-anchor="end">0</text>
    <rect x="348" y="96" width="24" height="72" fill="var(--dark)"/><rect x="398" y="65" width="24" height="103" fill="var(--orange)"/>
    <rect x="448" y="143" width="24" height="25" fill="var(--dark)"/><rect x="498" y="85" width="24" height="83" fill="var(--orange)"/>
    <text x="360" y="182" text-anchor="middle">JAN</text><text x="410" y="182" text-anchor="middle">FEB</text><text x="460" y="182" text-anchor="middle">MAR</text><text x="510" y="182" text-anchor="middle">APR</text>
    <g transform="translate(112 282) scale(1.45 .72)">
      <circle r="40" fill="none" stroke="#c46412" stroke-width="26" transform="translate(0 14)"/>
      <g transform="rotate(-90)" fill="none" stroke-width="26">
        <circle r="40" stroke="var(--orange)" stroke-dasharray="100.5 151"/>
        <circle r="40" stroke="var(--dark)" stroke-dasharray="0 100.5 50.3 101"/>
        <circle r="40" stroke="var(--orange)" stroke-dasharray="0 150.8 50.3 51"/>
        <circle r="40" stroke="var(--dark)" stroke-dasharray="0 201.1 50.3"/>
      </g>
    </g>
    <g font-size="11" font-weight="700" fill="#fff"><text x="62" y="290">40%</text><text x="122" y="252">20%</text><text x="160" y="285">20%</text><text x="118" y="320">20%</text></g>
    <circle cx="233" cy="228" r="3.5" fill="var(--orange)"/><circle cx="390" cy="228" r="3.5" fill="var(--dark)"/><circle cx="233" cy="270" r="3.5" fill="var(--dark)"/><circle cx="390" cy="270" r="3.5" fill="var(--orange)"/>
  </svg>
  <div class="abs" style="left:243px;top:222px;width:130px"><p class="it" style="font-size:8px">Lorem ipsum</p><p class="tx" style="font-size:5px">Growth in firms of fifty to five hundred staff this year.</p></div>
  <div class="abs" style="left:400px;top:222px;width:130px"><p class="it d" style="font-size:8px">Lorem ipsum</p><p class="tx" style="font-size:5px">New interest from retail and health groups in our region.</p></div>
  <div class="abs" style="left:243px;top:264px;width:130px"><p class="it d" style="font-size:8px">Lorem ipsum</p><p class="tx" style="font-size:5px">Remote teams that need clear tools for daily HR tasks.</p></div>
  <div class="abs" style="left:400px;top:264px;width:130px"><p class="it" style="font-size:8px">Lorem ipsum</p><p class="tx" style="font-size:5px">Partners ready to bundle our platform with their own offer.</p></div>
  <div class="foot"></div><div class="pg">07</div>
</section>

<!-- 08 Education -->
<section class="slide" style="left:364px;top:425px">
  <div class="brand"><span class="sq"></span>Corvexa</div>
  <h2 class="h2" style="left:25px;top:30px">Our company <span class="o">education</span></h2>
  <div class="abs" role="img" aria-label="Faint world map in the background" style="left:150px;top:60px;width:300px;height:190px;background:#f6f6f6;border-radius:40px"></div>
  <svg class="abs" style="left:0;top:0" width="608" height="342">
    <rect x="75" y="92" width="143" height="143" rx="8" fill="none" stroke="var(--orange)" stroke-width="2" stroke-dasharray="6 4"/>
    <rect x="88" y="105" width="117" height="117" fill="var(--orange)"/>
    <rect x="240" y="92" width="143" height="143" rx="8" fill="none" stroke="var(--dark)" stroke-width="2" stroke-dasharray="6 4"/>
    <rect x="253" y="105" width="117" height="117" fill="var(--dark)"/>
    <rect x="405" y="92" width="143" height="143" rx="8" fill="none" stroke="var(--dark)" stroke-width="2"/>
    <rect x="418" y="105" width="117" height="117" fill="var(--dark)"/>
    <path d="M218 163H236M230 158l6 5-6 5" stroke="var(--orange)" stroke-width="1.8" fill="none"/>
    <path d="M383 163H401M395 158l6 5-6 5" stroke="var(--dark)" stroke-width="1.8" fill="none"/>
    <g stroke="#fff" stroke-width="1.5" fill="none">
      <path d="M146 125a8 8 0 1 1 -8 0M140 138h4"/><circle cx="146.5" cy="129" r="8"/>
      <rect x="301" y="122" width="20" height="14"/><path d="M301 122l10 8 10-8"/>
      <path d="M468 122v16h18M472 134l10-10M477 124h5v5"/>
    </g>
    <g fill="#fff" text-anchor="middle" font-weight="700">
      <text x="146" y="157" font-size="10">IDEA</text><text x="311" y="157" font-size="10">PROMOTION</text><text x="476" y="157" font-size="10">GROWTH</text>
      <g font-size="5.5" font-weight="600"><text x="146" y="168">Spot the need and shape</text><text x="146" y="175">a clear plan for the</text><text x="146" y="182">whole team to follow</text>
      <text x="311" y="168">Share the plan with</text><text x="311" y="175">staff and leaders through</text><text x="311" y="182">short guided sessions</text>
      <text x="476" y="168">Track results, learn</text><text x="476" y="175">from feedback and scale</text><text x="476" y="182">what works best</text></g>
    </g>
  </svg>
  <p class="abs tx center" style="left:70px;top:262px;width:470px">Our learning programs guide every employee from first idea to lasting growth. Short, practical sessions help teams build new skills, share what they learn and turn knowledge into real results across the whole company.</p>
  <div class="foot"></div><div class="pg">08</div>
</section>

<!-- 09 Domain -->
<section class="slide" style="left:680px;top:425px">
  <div class="brand"><span class="sq"></span>Corvexa</div>
  <h2 class="h2" style="left:30px;top:55px;font-size:20px">Lorem ipsum<b>dolor sit amet</b></h2>
  <div class="abs" style="left:30px;top:110px;width:282px">
    <p class="tx">A clear online home builds trust with candidates and clients. Your careers page is often the first place great people meet your brand, so it must be fast, friendly and easy to find from any search or link.</p>
    <p class="tx">We help you set up pages that tell your story and invite the right people to apply.</p>
  </div>
  <div class="abs tri" style="left:30px;top:232px;width:282px"><i></i><p class="tx">Branded job pages that match your colours and your voice.</p></div>
  <div class="abs tri" style="left:30px;top:274px;width:282px"><i class="hollow"></i><p class="tx">Simple links that candidates can share with friends.</p></div>
  <div class="abs" style="left:340px;top:55px;font-size:15px;line-height:1.3;font-weight:500;color:var(--dark)">WHAT'S A DOMAIN?<br>IT'S THAT NAME UP<br><span style="color:var(--orange);font-weight:700">IN THE ADDRESS BAR.</span></div>
  <ul class="abs" style="left:340px;top:146px;list-style:none;font-size:10px;line-height:26px;color:var(--text)">
    <li><span style="color:var(--orange);margin-right:12px">✓</span>Fits your business or products</li>
    <li><span style="color:var(--orange);margin-right:12px">✓</span>Is easy to spell and remember</li>
    <li><span style="color:var(--orange);margin-right:12px">✓</span>Fits your business or products</li>
    <li><span style="color:var(--orange);margin-right:12px">✓</span>Is easy to spell and remember</li>
    <li><span style="color:var(--orange);margin-right:12px">✓</span>Fits your business or products</li>
    <li><span style="color:var(--orange);margin-right:12px">✓</span>Is easy to spell and remember</li>
  </ul>
  <div class="foot"></div><div class="pg">09</div>
</section>

<!-- 10 Timeline -->
<section class="slide" style="left:48px;top:609px">
  <div class="brand"><span class="sq"></span>Corvexa</div>
  <h2 class="h2" style="left:62px;top:28px;font-size:20px">Timeline <span class="o">infographic</span></h2>
  <svg class="abs" style="left:0;top:0" width="608" height="342" font-size="7">
    <rect x="62" y="55" width="488" height="265" fill="#fff" stroke="#777" stroke-width="1"/>
    <rect x="62" y="58" width="111" height="16" fill="var(--dark)"/>
    <text x="117" y="70" fill="var(--orange)" font-size="11" font-weight="700" text-anchor="middle">2022</text>
    <g stroke="#e0e0e0" stroke-width=".7">
      <path d="M206 58V318M237 58V318M268 58V318M300 58V318M331 58V318M362 58V318M393 58V318M425 58V318M456 58V318M487 58V318M518 58V318"/>
      <path d="M62 78H550M62 118H550M62 158H550M62 200H550M62 222H550M62 243H550M62 263H550M62 283H550"/>
    </g>
    <g fill="var(--dark)"><rect x="175" y="58" width="29" height="16"/><rect x="207" y="58" width="29" height="16"/><rect x="269" y="58" width="29" height="16"/><rect x="301" y="58" width="29" height="16"/><rect x="363" y="58" width="29" height="16"/><rect x="394" y="58" width="29" height="16"/><rect x="457" y="58" width="29" height="16"/><rect x="488" y="58" width="29" height="16"/></g>
    <g fill="var(--orange)"><rect x="238" y="58" width="29" height="16"/><rect x="332" y="58" width="29" height="16"/><rect x="426" y="58" width="29" height="16"/><rect x="519" y="58" width="29" height="16"/></g>
    <g fill="#fff" text-anchor="middle" font-size="7.5"><text x="190" y="69">JAN</text><text x="221" y="69">FEB</text><text x="253" y="69">MAR</text><text x="284" y="69">APR</text><text x="316" y="69">MAY</text><text x="347" y="69">JUN</text><text x="378" y="69">JUL</text><text x="409" y="69">AUG</text><text x="440" y="69">SEP</text><text x="472" y="69">OCT</text><text x="503" y="69">NOV</text><text x="534" y="69">DEC</text></g>
    <rect x="66" y="80" width="102" height="9" fill="var(--orange)"/><text x="73" y="87" fill="#fff" font-size="6" font-weight="700">● PHASE 1 TITLE</text>
    <rect x="175" y="81" width="110" height="6" rx="3" fill="var(--orange)"/>
    <g fill="var(--dark)" font-size="6.5" font-weight="700"><text x="70" y="101">Task 1</text><text x="70" y="141">Task 2</text><text x="70" y="182">Task 3</text></g>
    <g fill="#666" font-size="4.5"><text x="70" y="108">Draft the hiring plan</text><text x="70" y="113">with each team lead</text><text x="70" y="148">Run interviews and</text><text x="70" y="153">share quick feedback</text><text x="70" y="189">Welcome new starters</text><text x="70" y="194">and book training</text></g>
    <rect x="175" y="96" width="40" height="8" rx="4" fill="var(--orange)"/>
    <rect x="213" y="110" width="42" height="18" fill="#fff" stroke="var(--orange)" stroke-width=".8"/><text x="217" y="118" font-size="4" fill="#666">Plan signed off</text><text x="217" y="124" font-size="4" fill="#666">by all leads</text>
    <rect x="215" y="138" width="50" height="8" rx="4" fill="var(--orange)"/>
    <rect x="258" y="153" width="52" height="18" fill="#fff" stroke="var(--orange)" stroke-width=".8"/><text x="262" y="161" font-size="4" fill="#666">Shortlist ready</text><text x="262" y="167" font-size="4" fill="#666">for final round</text>
    <rect x="265" y="178" width="42" height="8" rx="4" fill="var(--orange)"/>
    <rect x="66" y="204" width="102" height="9" fill="var(--dark)"/><text x="73" y="211" fill="#fff" font-size="6" font-weight="700">● PHASE 2 TITLE</text>
    <rect x="290" y="205" width="155" height="6" fill="var(--dark)"/>
    <g fill="var(--dark)" font-size="6.5" font-weight="700"><text x="70" y="236">Task 1</text><text x="70" y="256">Task 2</text><text x="70" y="277">Task 3</text></g>
    <rect x="290" y="230" width="42" height="8" rx="4" fill="var(--dark)"/>
    <rect x="290" y="245" width="40" height="24" fill="#fff" stroke="var(--dark)" stroke-width=".8"/><text x="293" y="253" font-size="4" fill="#666">Review goals</text><text x="293" y="259" font-size="4" fill="#666">with staff</text>
    <rect x="330" y="250" width="80" height="8" rx="4" fill="var(--dark)"/>
    <rect x="350" y="271" width="70" height="8" rx="4" fill="var(--dark)"/>
  </svg>
  <div class="foot"></div><div class="pg">10</div>
</section>

<!-- 11 Use cases -->
<section class="slide" style="left:364px;top:609px">
  <div class="brand"><span class="sq"></span>Corvexa</div>
  <svg class="abs" style="left:0;top:0" width="608" height="342" fill="#fff" stroke="var(--dark)" stroke-width="2">
    <rect x="55" y="45" width="70" height="150" rx="8"/><rect x="142" y="92" width="70" height="150" rx="8"/><rect x="236" y="142" width="70" height="150" rx="8"/>
  </svg>
  <div class="abs" style="left:62px;top:62px;width:56px"><p style="font-size:9px;color:var(--dark)">Lorem ipsum dolor</p><p class="tx" style="font-size:4px;margin-top:40px">Guide new staff through their first days with clear steps and tips.</p></div>
  <div class="abs" style="left:149px;top:110px;width:56px"><p style="font-size:9px;color:var(--dark)">Dolor sit amet, conse</p><p class="tx" style="font-size:4px;margin-top:36px">Learn new skills with short lessons you can take on your phone.</p></div>
  <div class="abs" style="left:243px;top:160px;width:56px"><p style="font-size:9px;color:var(--dark)">Consec</p><p class="tx" style="font-size:4px;margin-top:36px">Finish a short quiz to earn your badge and share it with your team.</p></div>
  <h2 class="h2" style="left:335px;top:95px;font-size:40px;font-weight:600">Use <span class="o">cases</span></h2>
  <div class="abs" style="left:335px;top:146px;width:250px">
    <p class="tx">Teams use Corvexa every day to hire faster, welcome new people and grow skills. Managers approve leave in seconds, staff check pay and goals from their phones, and HR sees the whole picture in one calm view.</p>
    <p class="tx">From a shop floor to a global office, our tools adapt to how your people work and keep everyone on the same page.</p>
  </div>
  <div class="foot"></div><div class="pg">11</div>
</section>

<!-- 12 Stacked bars -->
<section class="slide" style="left:680px;top:609px">
  <div class="brand"><span class="sq"></span>Corvexa</div>
  <h2 class="h2" style="left:20px;top:28px;font-size:18px">Our company <span class="o">ipsum sit</span></h2>
  <svg class="abs" style="left:0;top:0" width="608" height="342" font-size="9" font-weight="600">
    <g fill="var(--orange)"><circle cx="46" cy="95" r="5"/><circle cx="46" cy="145" r="5"/><circle cx="46" cy="195" r="5"/></g>
    <g fill="var(--dark)" font-size="12"><text x="58" y="99">2019</text><text x="58" y="149">2020</text><text x="58" y="199">2021</text></g>
    <rect x="95" y="80" width="60" height="32" fill="var(--dark)"/><rect x="155" y="80" width="93" height="32" fill="var(--orange)"/><rect x="248" y="80" width="60" height="32" fill="var(--dark)"/><rect x="308" y="80" width="212" height="32" fill="var(--orange)"/>
    <rect x="95" y="130" width="150" height="32" fill="var(--orange)"/><rect x="245" y="130" width="105" height="32" fill="var(--dark)"/><rect x="350" y="130" width="85" height="32" fill="var(--orange)"/><rect x="435" y="130" width="85" height="32" fill="var(--dark)"/>
    <rect x="95" y="180" width="85" height="32" fill="var(--orange)"/><rect x="180" y="180" width="115" height="32" fill="var(--dark)"/><rect x="295" y="180" width="55" height="32" fill="var(--orange)"/><rect x="350" y="180" width="170" height="32" fill="var(--dark)"/>
    <g fill="#fff" text-anchor="middle"><text x="125" y="99">20%</text><text x="201" y="99">40%</text><text x="278" y="99">10%</text><text x="414" y="99">90%</text>
    <text x="170" y="149">50%</text><text x="297" y="149">30%</text><text x="392" y="149">20%</text><text x="477" y="149">20%</text>
    <text x="137" y="199">30%</text><text x="237" y="199">60%</text><text x="322" y="199">10%</text><text x="435" y="199">70%</text></g>
    <path d="M95 222H520" stroke="#999" stroke-width="1.5"/>
    <g fill="#999"><circle cx="95" cy="222" r="2.5"/><circle cx="137" cy="222" r="2.5"/><circle cx="180" cy="222" r="2.5"/><circle cx="222" cy="222" r="2.5"/><circle cx="265" cy="222" r="2.5"/><circle cx="307" cy="222" r="2.5"/><circle cx="350" cy="222" r="2.5"/><circle cx="392" cy="222" r="2.5"/><circle cx="435" cy="222" r="2.5"/><circle cx="477" cy="222" r="2.5"/><circle cx="520" cy="222" r="2.5"/></g>
    <g fill="var(--dark)" text-anchor="middle" font-size="8"><text x="95" y="237">0%</text><text x="137" y="237">10%</text><text x="180" y="237">20%</text><text x="222" y="237">30%</text><text x="265" y="237">40%</text><text x="307" y="237">50%</text><text x="350" y="237">60%</text><text x="392" y="237">70%</text><text x="435" y="237">80%</text><text x="477" y="237">90%</text><text x="520" y="237">100%</text></g>
  </svg>
  <div class="abs" style="left:88px;top:260px;width:95px"><p class="it" style="font-size:8px">LOREM IPSUM</p><p class="tx" style="font-size:5px">Share of time spent on hiring tasks each year.</p></div>
  <div class="abs" style="left:202px;top:260px;width:95px"><p class="it" style="font-size:8px">LOREM IPSUM</p><p class="tx" style="font-size:5px">Share of time spent on training and reviews.</p></div>
  <div class="abs" style="left:322px;top:260px;width:95px"><p class="it" style="font-size:8px">LOREM IPSUM</p><p class="tx" style="font-size:5px">Share of time spent on payroll and records.</p></div>
  <div class="abs" style="left:444px;top:260px;width:95px"><p class="it" style="font-size:8px">LOREM IPSUM</p><p class="tx" style="font-size:5px">Share of time spent on team wellbeing work.</p></div>
  <div class="foot"></div><div class="pg">12</div>
</section>

<!-- 13 Two columns -->
<section class="slide" style="left:48px;top:795px">
  <div class="brand"><span class="sq"></span>Corvexa</div>
  <div class="abs" style="left:30px;top:28px;width:283px;height:282px;background:var(--panel)"></div>
  <h2 class="h2" style="left:50px;top:40px;font-size:18px">Lorem ipsum<b>dolor sit amet</b></h2>
  <div class="abs" style="left:50px;top:86px;width:245px">
    <p class="tx">Our people team works side by side with yours to plan, hire and grow. We start with a short review of your current tools and goals, then build a clear road map that fits your budget and time.</p>
    <p class="tx">Each step is tested with real users, so the final setup feels natural from day one and saves hours every single week.</p>
  </div>
  <div class="abs tri" style="left:50px;top:210px;width:245px"><i></i><p class="tx">Fast setup with guided help from our own experts.</p></div>
  <div class="abs tri" style="left:50px;top:250px;width:245px"><i class="hollow"></i><p class="tx">Ongoing support and updates at no extra cost.</p></div>
  <h2 class="h2" style="left:330px;top:40px;font-size:18px">Lorem ipsum<b>dolor sit amet</b></h2>
  <div class="abs" style="left:330px;top:86px;width:250px">
    <p class="tx">Once live, our platform grows with you. Add new teams, sites or countries in minutes, and keep every policy and record in line with local rules through smart checks that run quietly in the background.</p>
    <p class="tx">Leaders get simple monthly reports with the key numbers that matter most, plus clear next steps they can take.</p>
  </div>
  <div class="abs tri" style="left:330px;top:210px;width:250px"><i style="border-left-color:var(--dark)"></i><p class="tx">Add new locations and teams in just a few clicks.</p></div>
  <div class="abs tri" style="left:330px;top:250px;width:250px"><i class="hollow"></i><p class="tx">Stay in line with local rules without extra effort.</p></div>
  <div class="foot"></div><div class="pg">13</div>
</section>

<!-- 14 Costs -->
<section class="slide" style="left:364px;top:795px">
  <div class="brand"><span class="sq"></span>Corvexa</div>
  <h2 class="h2" style="left:0;width:608px;top:38px;text-align:center;font-size:24px">Company <span class="o">costs</span></h2>
  <p class="abs tx center" style="left:35px;top:72px;width:540px">Our pricing is simple and open. You pay per active user, with no setup fees and no hidden extras, so budgets stay clear from the first month to the last.</p>
  <p class="abs tx center" style="left:45px;top:96px;width:520px">Plans scale as your company grows, and every plan includes updates, secure storage and friendly support.</p>
  <svg class="abs" style="left:0;top:0" width="608" height="342">
    <path d="M40 210H390" stroke="var(--orange)" stroke-width="5"/><path d="M390 210H568" stroke="var(--dark)" stroke-width="5"/>
    <path d="M568 204l8 6-8 6" fill="var(--dark)"/>
    <g fill="none" stroke-width="9">
      <circle cx="140" cy="177" r="28" stroke="var(--orange)" stroke-dasharray="150 26" transform="rotate(112 140 177)"/>
      <circle cx="248" cy="177" r="28" stroke="var(--dark)" stroke-dasharray="150 26" transform="rotate(112 248 177)"/>
      <circle cx="355" cy="177" r="28" stroke="var(--orange)" stroke-dasharray="150 26" transform="rotate(112 355 177)"/>
      <circle cx="462" cy="177" r="28" stroke="var(--dark)" stroke-dasharray="150 26" transform="rotate(112 462 177)"/>
    </g>
    <g stroke="var(--dark)" stroke-width="1.5" fill="none">
      <circle cx="140" cy="177" r="11"/><path d="M140 170v7l5 4"/>
      <circle cx="248" cy="179" r="11" fill="var(--orange)" stroke="var(--orange)"/>
      <ellipse cx="355" cy="170" rx="10" ry="3.5"/><path d="M345 170v14c0 2 4 4 10 4s10-2 10-4V170M345 177c0 2 4 4 10 4s10-2 10-4"/>
      <circle cx="459" cy="174" r="8" stroke="var(--orange)"/><path d="M465 180l7 7" stroke="var(--orange)" stroke-width="2.5"/>
    </g>
    <text x="248" y="183" fill="#fff" font-size="12" font-weight="700" text-anchor="middle">$</text>
    <g font-size="7" font-weight="700" fill="#fff" text-anchor="middle"><text x="180" y="213">Step 01</text><text x="288" y="213">Step 02</text><text x="395" y="213">Step 03</text><text x="502" y="213">Step 04</text></g>
    <g stroke="#777" stroke-width="1"><path d="M140 220v18M248 220v18M355 220v18M462 220v18"/></g>
  </svg>
  <div class="abs center" style="left:95px;top:244px;width:90px"><p class="it d" style="font-size:10px">Lorem Ipsum</p><p class="tx center" style="font-size:5px;opacity:.7">Book a short call to map out your needs and goals.</p></div>
  <div class="abs center" style="left:203px;top:244px;width:90px"><p class="it" style="font-size:10px">Lorem Ipsum</p><p class="tx center" style="font-size:5px;opacity:.7">Get a clear quote based on your active users.</p></div>
  <div class="abs center" style="left:310px;top:244px;width:90px"><p class="it d" style="font-size:10px">Lorem Ipsum</p><p class="tx center" style="font-size:5px;opacity:.7">Move your records over safely with our team.</p></div>
  <div class="abs center" style="left:417px;top:244px;width:90px"><p class="it" style="font-size:10px">Lorem Ipsum</p><p class="tx center" style="font-size:5px;opacity:.7">Go live and review results after the first month.</p></div>
  <div class="foot"></div><div class="pg">14</div>
</section>

<!-- 15 Benefits -->
<section class="slide" style="left:680px;top:795px">
  <div class="brand"><span class="sq"></span>Corvexa</div>
  <div class="photo" role="img" aria-label="Photo of smiling colleagues working together at a computer" style="left:30px;top:50px;width:262px;height:250px;background:linear-gradient(135deg,#e6e8ea,#c5bcb2 55%,#8d8780)"></div>
  <h2 class="h2" style="left:310px;top:50px;font-size:18px">Benefits to each<b>customer segments</b></h2>
  <div class="abs" style="left:310px;top:96px;width:270px">
    <p class="tx">Small teams get a ready setup that works on day one, with no IT staff needed and a price that fits a tight budget.</p>
    <p class="tx">Growing firms gain simple hiring flows and clear reports that keep pace as new teams and offices are added.</p>
    <p class="tx">Large groups get strong controls, custom roles and links to the tools they already use across many regions.</p>
    <p class="tx">Public bodies rely on secure storage, open audit trails and support for local rules in every step.</p>
    <p class="tx">Every client gets friendly help, regular updates and a team that truly cares about their people.</p>
  </div>
  <div class="foot"></div><div class="pg">15</div>
</section>

<!-- 16 Advisors -->
<section class="slide" style="left:48px;top:982px">
  <div class="brand"><span class="sq"></span>Corvexa</div>
  <div class="abs" style="left:212px;top:62px;width:173px;height:280px;background:var(--panel)"></div>
  <h2 class="h2" style="left:35px;top:72px;font-size:14px">Active advisors<b style="font-size:17px">and members</b></h2>
  <div class="abs" style="left:35px;top:112px;width:165px">
    <p class="tx">Our advisors bring years of HR, finance and tech work to every project. They guide plans, check results and share advice that helps our clients grow with care and confidence.</p>
    <p class="tx">Each member meets clients often to keep goals clear, listen to feedback and shape the next steps of our shared work together.</p>
    <p class="tx">They also mentor our own staff and help new hires grow fast.</p>
  </div>
  <h2 class="h2" style="left:224px;top:72px;font-size:14px">Active advisors<b style="font-size:17px">and members</b></h2>
  <div class="abs" style="left:224px;top:112px;width:150px">
    <p class="tx">Our board includes leaders from retail, health and tech. They test new ideas, review our roadmap and make sure every tool we build solves a real need for real teams.</p>
    <p class="tx">Together they keep Corvexa focused on fair, simple and human HR for companies of every size, in every region we serve today.</p>
    <p class="tx">Their advice shapes each new release we ship.</p>
  </div>
  <h2 class="h2" style="left:406px;top:72px;font-size:14px">Active advisors<b style="font-size:17px">and members</b></h2>
  <div class="abs" style="left:406px;top:112px;width:168px">
    <p class="tx">Our members group brings clients together to share what works. They join short calls, test early features and tell us plainly what to improve next for their teams.</p>
    <p class="tx">This open loop keeps our products grounded in daily work and helps every member learn from peers facing the same people challenges as them.</p>
    <p class="tx">New members are always welcome to join us.</p>
  </div>
  <div class="foot"></div><div class="pg">16</div>
</section>

<!-- 17 Team -->
<section class="slide" style="left:364px;top:982px">
  <div class="brand"><span class="sq"></span>Corvexa</div>
  <h2 class="h2" style="left:0;width:608px;top:45px;text-align:center;font-size:18px">Team members <span class="o">and advisors</span></h2>
  <p class="abs tx center" style="left:40px;top:72px;width:528px">Meet the people behind Corvexa. Our team blends HR know-how with strong tech skills, and every member is here to help your people thrive at work.</p>
  <p class="abs tx center" style="left:40px;top:104px;width:528px">We are proud to work with clients who share our care for fair and simple HR.</p>
  <div class="abs" style="left:0;top:138px;width:608px;height:152px;background:var(--orange)"></div>
  <svg class="abs" style="left:0;top:0" width="608" height="342">
    <g stroke="var(--dark)" stroke-width="2">
      <circle cx="87" cy="178" r="24" fill="#f2dccb" role="img" aria-label="Portrait of team member"/>
      <circle cx="233" cy="178" r="24" fill="#f2dccb" role="img" aria-label="Portrait of team member"/>
      <circle cx="376" cy="178" r="24" fill="#f2dccb" role="img" aria-label="Portrait of team member"/>
      <circle cx="522" cy="178" r="24" fill="#f2dccb" role="img" aria-label="Portrait of team member"/>
    </g>
  </svg>
  <div class="abs center" style="left:42px;top:208px;width:90px"><p style="font-size:9px;font-weight:700;color:#fff">JOHN SMITH</p><p class="tx center" style="font-size:4.5px;color:#fff">Leads our product team and shapes each new tool we build for clients.</p></div>
  <div class="abs center" style="left:188px;top:208px;width:90px"><p style="font-size:9px;font-weight:700;color:var(--dark)">MILLIE SMITH</p><p class="tx center" style="font-size:4.5px;color:#fff">Runs client success and makes sure every launch goes smoothly.</p></div>
  <div class="abs center" style="left:331px;top:208px;width:90px"><p style="font-size:9px;font-weight:700;color:var(--dark)">JOHN SMITH</p><p class="tx center" style="font-size:4.5px;color:#fff">Heads our data team and turns people numbers into clear insight.</p></div>
  <div class="abs center" style="left:477px;top:208px;width:90px"><p style="font-size:9px;font-weight:700;color:var(--dark)">MILLIE SMITH</p><p class="tx center" style="font-size:4.5px;color:#fff">Advises on HR policy and helps clients stay in line with local rules.</p></div>
  <div class="foot"></div><div class="pg">14</div>
</section>

<!-- 18 Contact -->
<section class="slide" style="left:680px;top:982px">
  <div class="abs" style="left:52px;top:88px;font-size:40px;font-weight:600;color:var(--dark);display:flex;align-items:center;gap:10px"><span class="sq" style="width:18px;height:18px"></span>Corvexa</div>
  <h2 class="h2" style="left:40px;top:198px;font-size:24px;font-weight:700">Contact <span class="o">us</span></h2>
  <svg class="abs" style="left:0;top:0" width="608" height="342" fill="var(--orange)">
    <circle cx="47" cy="248" r="5"/><circle cx="47" cy="272" r="5"/><circle cx="47" cy="296" r="5"/>
    <path d="M45 246l1 2-1 1 2 2 1-1 2 1-1 2c-2 0-5-3-5-5z" fill="#fff"/>
    <rect x="44" y="270" width="6" height="4" fill="#fff"/>
    <circle cx="47" cy="295" r="1.8" fill="#fff"/>
  </svg>
  <div class="abs" style="left:62px;top:240px;font-size:13px;line-height:24px;color:var(--dark)">
    <p>555-010-0199</p>
    <p>hello@corvexa-example.com</p>
    <p>Your address, your city, box 88900</p>
  </div>
</section>

</div>
</body>
</html>
```